Tidewell Recovery Business Card Design

Professional and clean design. The design colors should flow with the logo. Two-sided card with the website on the back which is:

www.TidewellRecovery.example.

"Specializing in Water Damage Restoration"

On the front I need the name, email, phone, and logo.

Name: Dorian Vashti
Email: Dorian@TidewellRecovery.example
Phone: 555-318-2046 for now

I only have the Preview and Thumbnail right now but should have the source files uploaded within a day or two.

Target Market(s)

Flood victims, home owners with water damage from busted pipes etc...

Industry/Entity Type

Business

Contact Information for Business Card

Name: Dorian Vashti

Font styles to use
Serif
Sans Serif

```html
<!DOCTYPE html>
<html lang="en">
<head>
<meta charset="utf-8">
<title>Tidewell Recovery Business Card</title>
<link rel="stylesheet" href="https://fonts.googleapis.com/css2?family=Cinzel:wght@600&family=Open+Sans:wght@400&family=Arimo:wght@700&display=swap">
<style>
  :root {
    --blue-deep: #2b96d3;
    --blue-light: #56c1ef;
    --card-white: #ffffff;
    --backdrop: #eceae6;
  }
  * { margin: 0; padding: 0; box-sizing: border-box; }
  html, body {
    width: 960px;
    height: 1200px;
    overflow: hidden;
    background: var(--backdrop);
  }
  .card {
    position: absolute;
    left: 106px;
    width: 746px;
    height: 455px;
    background: var(--card-white);
    overflow: hidden;
    box-shadow: 0 10px 24px rgba(0,0,0,0.18);
  }
  .card--back { top: 61px; }
  .card--front { top: 684px; }

  .stripes {
    position: absolute;
    left: 0; top: 0;
    width: 100%;
    height: 38px;
    background: linear-gradient(to bottom,
      var(--blue-deep) 0 9px,
      var(--card-white) 9px 13px,
      var(--blue-light) 13px 22px,
      var(--card-white) 22px 28px,
      var(--blue-deep) 28px 38px);
  }
  .base-band {
    position: absolute;
    left: 0; bottom: 0;
    width: 100%;
    height: 36px;
    background: var(--blue-deep);
  }

  /* Back side */
  .back-brand {
    position: absolute;
    left: 0; top: 96px;
    width: 100%;
    text-align: center;
  }
  .brand-dot {
    display: block;
    margin: 0 auto;
    border-radius: 50%;
    background: var(--blue-light);
  }
  .back-brand .brand-dot { width: 110px; height: 110px; }
  .back-brand .brand-name {
    margin-top: 18px;
    font-family: "Cinzel", serif;
    font-weight: 600;
    font-size: 28px;
    letter-spacing: 1px;
    color: var(--blue-deep);
  }
  .back-website {
    position: absolute;
    left: 0; top: 301px;
    width: 100%;
    text-align: center;
    font-family: "Open Sans", sans-serif;
    font-size: 27px;
    color: var(--blue-light);
  }

  /* Front side */
  .holder-name {
    position: absolute;
    left: 44px; top: 88px;
    font-family: "Cinzel", serif;
    font-weight: 600;
    font-size: 31px;
    letter-spacing: 0.5px;
    color: var(--blue-light);
  }
  .contact-list {
    position: absolute;
    left: 46px; top: 168px;
    list-style: none;
  }
  .contact-item {
    display: flex;
    align-items: center;
    height: 30px;
    margin-bottom: 50px;
    font-family: "Arimo", sans-serif;
    font-weight: 700;
    font-size: 14px;
    color: var(--blue-light);
  }
  .contact-item:nth-child(2) { margin-bottom: 46px; }
  .contact-icon {
    width: 28px;
    height: 28px;
    margin-right: 15px;
    flex: none;
  }
  .front-brand {
    position: absolute;
    left: 430px; top: 118px;
    width: 268px;
    text-align: center;
  }
  .front-brand .brand-dot { width: 140px; height: 140px; }
  .front-brand .brand-name {
    margin-top: 16px;
    font-family: "Cinzel", serif;
    font-weight: 600;
    font-size: 28px;
    line-height: 1.05;
    color: var(--blue-deep);
  }
</style>
</head>
<body>

<section class="card card--back" aria-label="Card back">
  <div class="stripes"></div>
  <div class="back-brand">
    <span class="brand-dot"></span>
    <p class="brand-name">Tidewell Recovery</p>
  </div>
  <p class="back-website">www.TidewellRecovery.example</p>
  <div class="base-band"></div>
</section>

<section class="card card--front" aria-label="Card front">
  <div class="stripes"></div>
  <h1 class="holder-name">DORIAN VASHTI</h1>
  <ul class="contact-list">
    <li class="contact-item">
      <svg class="contact-icon" viewBox="0 0 24 24" aria-hidden="true">
        <path fill="#56c1ef" d="M6.6 2.5c.6-.4 1.4-.2 1.8.4l2 3.3c.4.6.2 1.4-.3 1.8l-1.5 1.1c.9 2.2 2.6 4.1 4.8 5.3l1.2-1.4c.4-.5 1.2-.7 1.8-.3l3.3 1.9c.6.4.8 1.2.5 1.8l-1.2 2.3c-.5.9-1.6 1.4-2.6 1.1C9.8 18.3 5 13.3 3.6 6.7c-.2-1 .2-2 1.1-2.6z"/>
      </svg>
      <span>555-318-2046</span>
    </li>
    <li class="contact-item">
      <svg class="contact-icon" viewBox="0 0 24 24" aria-hidden="true">
        <rect x="2.5" y="5.5" width="19" height="13" fill="none" stroke="#56c1ef" stroke-width="1.6"/>
        <path d="M2.5 5.5l9.5 7.5 9.5-7.5M2.5 18.5l7-6M21.5 18.5l-7-6" fill="none" stroke="#56c1ef" stroke-width="1.6"/>
      </svg>
      <span>Dorian@TidewellRecovery.example</span>
    </li>
    <li class="contact-item">
      <svg class="contact-icon" viewBox="0 0 24 24" aria-hidden="true">
        <g fill="none" stroke="#56c1ef" stroke-width="1.6">
          <circle cx="11" cy="11" r="8.5"/>
          <ellipse cx="11" cy="11" rx="3.8" ry="8.5"/>
          <path d="M2.5 11h17M4 6.5h14M4 15.5h14"/>
        </g>
        <path fill="#2b96d3" d="M14 13l8 3.2-3.3 1.1 2.6 3-1.3 1.1-2.6-3-1.6 3z"/>
      </svg>
      <span>www.TidewellRecovery.example</span>
    </li>
  </ul>
  <div class="front-brand">
    <span class="brand-dot"></span>
    <p class="brand-name">TIDEWELL<br>RECOVERY</p>
  </div>
  <div class="base-band"></div>
</section>

</body>
</html>
```